New Interfaces

The software open with 3 open tabs, you can see the interfaces following this steps:

Brindle:
Select tab "Brindle" and click on "Brindle" in menu on the top.

KPI :
Select tab "KPI" and click on go button.

Report:
Select tab "Report" and Click on go button.

Current software: http://volteq.vextal-example.com/volteq_developers/default.aspx

user: sample_guest
pass: plinkaa

......

About the company

The VexTal is a technology company that provides planning, optimization services and software to develop the market for telecom operators.

The Product

Volteq is a web management and optimization tool for mobile networks.

The project

To always offer the best experience of usability and comfort for our customers, we are remodeling our software. The goal is to have agile, modern and with special attention to usability interfaces.

user: sample_guest
pass: plinkaa

Hi! We are analyzing all interfaces, we send news soon. Thank you!

Target Market(s)

Telecommunications Engineers.

Industry/Entity Type

Software

Font styles to use
Sans Serif

Requirements
Nice to have
• Attention for usability and good concept.
Should not have
• Many colors.

```html
<!DOCTYPE html>
<html lang="en">
<head>
<meta charset="utf-8">
<title>Volteq – Network Workspace</title>
<link href="https://fonts.googleapis.com/css2?family=Roboto:wght@400;500;700&display=swap" rel="stylesheet">
<style>
  :root{
    --orange:#e07f35;
    --dark:#232323;
    --dark-btn:#343434;
    --blue:#00568a;
    --blue-icon:#1a8fd6;
    --white:#ffffff;
    --page:#f5f5f5;
    --panel:#fafafa;
    --line:#e6e6e6;
    --text:#4a4a4a;
    --muted:#bdbdbd;
    --brand:#2b5c94;
  }
  *{box-sizing:border-box;margin:0;padding:0}
  html,body{width:1200px;height:960px;overflow:hidden}
  body{font-family:"Roboto",Arial,sans-serif;background:var(--page);color:var(--text);position:relative}

  .brand{position:absolute;left:0;top:0;width:300px;height:110px;background:var(--white);display:flex;align-items:center;justify-content:center;gap:10px}
  .brand-mark{width:14px;height:14px;border-radius:50%;background:var(--brand)}
  .brand-name{font-size:30px;font-weight:700;color:var(--brand);letter-spacing:.5px}

  .topnav{position:absolute;left:300px;top:0;width:611px;height:110px;background:var(--dark);border-bottom:6px solid var(--orange)}
  .topnav-item{position:absolute;top:30px;height:50px;display:flex;align-items:center;color:var(--white);font-size:17px;letter-spacing:.3px}
  .topnav-item.is-active{left:68px;width:106px;justify-content:center;background:var(--dark-btn)}
  .topnav-item.notes{left:280px}
  .topnav-item.historic{left:445px;gap:14px}
  .topnav-sep{position:absolute;top:42px;width:1px;height:26px;background:#444}

  .treeview{position:absolute;left:911px;top:0;width:289px;height:116px;background:var(--orange);color:var(--white);font-weight:500;font-size:17px;letter-spacing:.3px}
  .treeview-label{position:absolute;left:72px;top:46px}
  .treeview svg{position:absolute;left:198px;top:48px}

  .sidebar{position:absolute;left:0;top:110px;width:300px;height:850px;background:var(--white)}
  .side-row{height:89px;border-bottom:1px solid var(--line);display:flex;align-items:center;position:relative;font-size:15px;font-weight:500;letter-spacing:.2px;color:var(--text)}
  .side-icon{width:72px;height:100%;border-right:1px solid var(--line);display:flex;align-items:center;justify-content:center}
  .side-label{padding-left:17px;flex:1}
  .side-chevron{position:absolute;right:22px;top:38px}
  .side-row.is-real{background:var(--orange);color:var(--white);font-weight:700;height:90px;border-bottom:none}
  .side-row.is-real .side-icon{border-right-color:rgba(255,255,255,.25)}
  .side-row.is-planned{background:var(--blue);color:var(--white);font-weight:700;height:90px;border-bottom:none}
  .side-row.is-planned .side-icon{border-right-color:rgba(255,255,255,.2)}
  .side-row.is-empty{border-top:1px solid var(--line)}
  .vendor-dot{width:12px;height:12px;border-radius:50%;background:#9a9a9a}

  .tabbar{position:absolute;left:300px;top:116px;width:900px;height:117px;background:var(--page)}
  .tab{position:absolute;left:0;top:0;width:168px;height:117px;background:var(--white);display:flex;align-items:center;justify-content:center;font-size:17px;font-weight:500;color:var(--text);letter-spacing:.3px}
  .zoom{position:absolute;width:34px;height:34px;border:1.5px solid #d3d3d3;border-radius:50%;top:42px;display:flex;align-items:center;justify-content:center;color:var(--muted);font-size:15px}
  .zoom.out{left:201px}
  .zoom.in{left:242px}
  .tab-input{position:absolute;left:288px;top:72px;width:494px;height:2px;background:#cfcfcf}
  .new-tab{position:absolute;right:0;top:0;width:85px;height:117px;background:var(--white);display:flex;flex-direction:column;align-items:center;padding-top:26px;font-size:14px;color:var(--text);gap:12px}
  .new-tab-circle{width:38px;height:38px;border:2px solid #555;border-radius:50%;display:flex;align-items:center;justify-content:center;font-size:18px;color:#444}

  .workspace{position:absolute;left:324px;top:235px;width:852px;height:679px;background:var(--panel);border:1px solid var(--line)}
</style>
</head>
<body>
  <header>
    <div class="brand"><span class="brand-mark"></span><span class="brand-name">VexTal</span></div>
    <nav class="topnav">
      <div class="topnav-item is-active">GO ALL</div>
      <span class="topnav-sep" style="left:226px"></span>
      <div class="topnav-item notes">NOTES</div>
      <span class="topnav-sep" style="left:391px"></span>
      <div class="topnav-item historic">HISTORIC
        <svg width="10" height="8" viewBox="0 0 10 8"><path d="M0 0h10L5 7z" fill="#fff"/></svg>
      </div>
    </nav>
    <div class="treeview">
      <span class="treeview-label">TREEVIEW</span>
      <svg width="18" height="14" viewBox="0 0 18 14"><path d="M0 0h18L9 14z" fill="#fff"/></svg>
    </div>
  </header>

  <aside class="sidebar">
    <div class="side-row is-real">
      <div class="side-icon">
        <svg width="30" height="30" viewBox="0 0 30 30" fill="none" stroke="#fff" stroke-width="1.4" opacity=".85">
          <circle cx="14" cy="14" r="11"/><ellipse cx="14" cy="14" rx="5" ry="11"/><path d="M3 14h22M5 8h18M5 20h18"/>
          <rect x="19" y="19" width="8" height="8" fill="#fff" stroke="none"/>
        </svg>
      </div>
      <span class="side-label">REAL NETWORK</span>
      <svg class="side-chevron" width="16" height="10" viewBox="0 0 16 10"><path d="M1 9l7-7 7 7" stroke="#fff" stroke-width="1.8" fill="none"/></svg>
    </div>
    <div class="side-row"><div class="side-icon"><span class="vendor-dot"></span></div><span class="side-label">TARROW</span><svg class="side-chevron" width="16" height="10" viewBox="0 0 16 10"><path d="M1 1l7 7 7-7" stroke="#555" stroke-width="1.8" fill="none"/></svg></div>
    <div class="side-row"><div class="side-icon"><span class="vendor-dot"></span></div><span class="side-label">PELLUM</span><svg class="side-chevron" width="16" height="10" viewBox="0 0 16 10"><path d="M1 1l7 7 7-7" stroke="#555" stroke-width="1.8" fill="none"/></svg></div>
    <div class="side-row"><div class="side-icon"><span class="vendor-dot"></span></div><span class="side-label">QUORRA</span><svg class="side-chevron" width="16" height="10" viewBox="0 0 16 10"><path d="M1 1l7 7 7-7" stroke="#555" stroke-width="1.8" fill="none"/></svg></div>
    <div class="side-row"><div class="side-icon"><span class="vendor-dot"></span></div><span class="side-label">BRISKO</span><svg class="side-chevron" width="16" height="10" viewBox="0 0 16 10"><path d="M1 1l7 7 7-7" stroke="#555" stroke-width="1.8" fill="none"/></svg></div>
    <div class="side-row"><div class="side-icon"><span class="vendor-dot"></span></div><span class="side-label">MULTIVENDOR</span><svg class="side-chevron" width="16" height="10" viewBox="0 0 16 10"><path d="M1 1l7 7 7-7" stroke="#555" stroke-width="1.8" fill="none"/></svg></div>
    <div class="side-row"><div class="side-icon"><span class="vendor-dot"></span></div><span class="side-label">ODENFEL</span><svg class="side-chevron" width="16" height="10" viewBox="0 0 16 10"><path d="M1 1l7 7 7-7" stroke="#555" stroke-width="1.8" fill="none"/></svg></div>
    <div class="side-row"><div class="side-icon"><span class="vendor-dot"></span></div><span class="side-label">KESTRIN</span><svg class="side-chevron" width="16" height="10" viewBox="0 0 16 10"><path d="M1 1l7 7 7-7" stroke="#555" stroke-width="1.8" fill="none"/></svg></div>
    <div class="side-row is-planned">
      <div class="side-icon">
        <svg width="30" height="30" viewBox="0 0 30 30" fill="none" stroke="var(--blue-icon)" stroke-width="2.4">
          <circle cx="15" cy="15" r="12"/><circle cx="15" cy="15" r="6"/><path d="M15 15l9-9"/>
        </svg>
      </div>
      <span class="side-label">PLANNED NETWORK</span>
      <svg class="side-chevron" width="16" height="10" viewBox="0 0 16 10"><path d="M1 1l7 7 7-7" stroke="#fff" stroke-width="1.8" fill="none" opacity=".7"/></svg>
    </div>
    <div class="side-row is-empty"><div class="side-icon"></div></div>
  </aside>

  <section class="tabbar">
    <div class="tab">NEW TAB</div>
    <span class="zoom out">-</span>
    <span class="zoom in">+</span>
    <span class="tab-input"></span>
    <div class="new-tab"><span class="new-tab-circle">+</span>NEW</div>
  </section>

  <main class="workspace"></main>
</body>
</html>
```